Business cards and stationary for a health and wellbeing company
Lumen Forms
Business cards and stationary for a health and wellbeing company - Health
Creative Brief
Bright & Fun-filled
Jolene prescott
Director
PO Box
sales@lumenforms.com.au
www.lumenforms.com.au
Hi, I am happy to have a wide selection of fonts and designs. Lumen Forms is a health conscious Australian business that sells protein, supplements, health equipment, meditation and beauty products. We pride ourselves on great customer service, great products and a true passion for feeling and looking good. Our target market is females aged 18-60 years of age, mums and woman who want to feel amazing. Colour • Pink • White • Blue • Purple
Im open to different designs.
JolenePrescott JolenePrescott
Hi Everyone, Thank you so much for your great designs! I love the bright colours and lines that flow rather than straight and sharp. Could you please show me the front as well as the back of the business cards. I am wanting to change the font on my logo? I am wanting it so that the word Lumen sits above the word forms. Looking forward to some great designs! Thanks!

```html
<!DOCTYPE html>
<html lang="en">
<head>
<meta charset="utf-8">
<title>Lumen Forms – Business Card</title>
<link href="https://fonts.googleapis.com/css2?family=Nunito:wght@800&family=Tinos&display=swap" rel="stylesheet">
<style>
  :root {
    --magenta: #c7239b;
    --magenta-deep: #a8137f;
    --sky: #27b4e6;
    --white: #ffffff;
    --ink: #3a3a3a;
    --backdrop: #e9e9ec;
  }
  * { margin: 0; padding: 0; box-sizing: border-box; }
  html, body { width: 1200px; height: 901px; overflow: hidden; }
  body { background: var(--backdrop); position: relative; font-family: "Tinos", serif; }

  .card {
    position: absolute;
    top: 295px;
    width: 540px;
    height: 310px;
    border-radius: 24px;
    background: var(--white);
    overflow: hidden;
    box-shadow: 0 6px 18px rgba(0,0,0,0.12);
  }
  .card--front { left: 45px; }
  .card--back { left: 615px; }
  .card__waves { position: absolute; inset: 0; }

  .brand {
    position: absolute;
    display: flex;
    flex-direction: column;
    align-items: center;
    gap: 8px;
  }
  .brand__dot {
    width: 44px; height: 44px; border-radius: 50%;
    background: var(--magenta);
  }
  .brand__name {
    font-family: "Nunito", sans-serif;
    font-weight: 800;
    font-size: 30px;
    letter-spacing: -0.5px;
    color: var(--magenta);
    white-space: nowrap;
  }
  .card--front .brand { left: 260px; top: 42px; width: 250px; }
  .card--back .brand { left: 0; right: 0; top: 95px; }
  .card--back .brand__dot { width: 58px; height: 58px; }
  .card--back .brand__name { font-size: 38px; }

  .person {
    position: absolute;
    left: 260px; width: 250px; top: 146px;
    text-align: center;
    color: var(--ink);
  }
  .person__name { font-size: 24px; line-height: 1.1; }
  .person__title { font-size: 19px; line-height: 1.1; margin-top: 4px; }

  .contacts {
    position: absolute;
    left: 22px; top: 88px;
    list-style: none;
    color: var(--white);
    font-size: 11px;
    line-height: 1.35;
  }
  .contacts li { display: flex; align-items: flex-start; gap: 7px; margin-bottom: 9px; }
  .contacts .icon { width: 11px; height: 11px; flex: none; margin-top: 2px; }
</style>
</head>
<body>

<section class="card card--front">
  <svg class="card__waves" viewBox="0 0 540 310" aria-hidden="true">
    <path d="M0 0 H150 C170 140 215 225 310 255 S480 274 540 276 V310 H0 Z" fill="var(--magenta)"/>
    <path d="M122 0 C145 135 195 220 290 248 S470 264 540 264" fill="none" stroke="var(--sky)" stroke-width="8"/>
    <path d="M0 310 V292 C120 302 320 306 540 290 V310 Z" fill="var(--magenta-deep)" opacity="0.35"/>
  </svg>

  <ul class="contacts">
    <li>
      <svg class="icon" viewBox="0 0 12 12"><path d="M6 0 C3 0 1.5 2 1.5 4.2 C1.5 7 6 12 6 12 C6 12 10.5 7 10.5 4.2 C10.5 2 9 0 6 0 Z" fill="var(--white)"/><circle cx="6" cy="4.3" r="1.6" fill="var(--magenta)"/></svg>
      <span>Suite # 410, Elm Bldg.<br>NY 10012</span>
    </li>
    <li>
      <svg class="icon" viewBox="0 0 12 12"><path d="M2 0 L4.5 0 L5.5 3 L4 4.2 C5 6.2 5.8 7 7.8 8 L9 6.5 L12 7.5 L12 10 C12 11 11 12 10 12 C4.5 11.5 0.5 7.5 0 2 C0 1 1 0 2 0 Z" fill="var(--white)"/></svg>
      <span>(555) 014-2237<br>555-019-4480<br>555-013-7725</span>
    </li>
    <li>
      <svg class="icon" viewBox="0 0 12 12"><rect x="0" y="2" width="12" height="8" rx="1" fill="var(--white)"/><path d="M0.5 2.5 L6 6.5 L11.5 2.5" fill="none" stroke="var(--magenta)" stroke-width="1"/></svg>
      <span>hello@lumenforms.com.au<br>www.lumenforms.com.au</span>
    </li>
  </ul>

  <div class="brand">
    <span class="brand__dot"></span>
    <span class="brand__name">Lumen Forms</span>
  </div>

  <div class="person">
    <p class="person__name">Ellis Marlowe</p>
    <p class="person__title">Owner / C.E.O</p>
  </div>
</section>

<section class="card card--back">
  <div class="brand">
    <span class="brand__dot"></span>
    <span class="brand__name">Lumen Forms</span>
  </div>
</section>

</body>
</html>
```